Business Card Design Project

We have recently completed MakerHive projects for a new logo and wesbite.
We now require new business cards.
We hand out very little printed material to clients as all information is online. When we do hand out something, like a business card, we want it to have real impact and make a statement about the quality and professionalism of our company.
We have an idea of what we want our card to look like but we want a designer to make sure they have impact and look great.
Our requirements are…
Size: 85mm X 55mm - Landscape
Front of card: Logo plus the following contact information.
Derek Fenwick
Operations Manager
Phone +44(0) 1632 xxx xxx
Mobile +44(0) 7700 xxx xxx
Email derekf@corebitsys.example
Address 19 Tarlow Street, Aberdeen AB12 4QP
Website www.corebitsys.example
How you layout the front of the card is up to you, we would like to see some different ideas. Attached are two versions of our logo that may be used.
Back of card: We would like this to be simple but again have impact. Our current thought is to have the logo or just the large W design from the logo in white against a dark background, perhaps made up from the dark green in the logo.
The logos are attached so you can see the colours in them but the dark ones are..
Dark Blue = C:88, M:55, Y:44, K:28
Dark Green = C:87, M:53, Y:50, K:50
We sometimes also use a bright orange as an accent or highlight colour…
Orange: = C:0, M:39, Y:94, K:0

```html
<!DOCTYPE html>
<html lang="en">
<head>
<meta charset="utf-8">
<title>CoreBit Systems – Business Cards</title>
<link rel="stylesheet" href="https://fonts.googleapis.com/css2?family=Ubuntu:wght@400;500;700&display=swap">
<style>
  :root {
    --page-bg: #e6e7e8;
    --card-white: #ffffff;
    --dark-teal: #275368;
    --teal-text: #2f5d70;
    --ink: #1f2a30;
    --rule: #3f6f82;
    --accent-green: #7f9a3a;
  }
  * { margin: 0; padding: 0; box-sizing: border-box; }
  html, body {
    width: 1200px;
    height: 900px;
    overflow: hidden;
    background: var(--page-bg);
    font-family: "Ubuntu", sans-serif;
  }
  .card {
    position: absolute;
    width: 540px;
    height: 350px;
    border-radius: 3px;
    box-shadow: 0 10px 24px rgba(0,0,0,0.18);
    overflow: hidden;
  }
  .card--back {
    left: 330px;
    top: 70px;
    background: var(--dark-teal);
    display: flex;
    align-items: center;
    justify-content: center;
  }
  .card--front {
    left: 330px;
    top: 475px;
    background: var(--card-white);
  }
  .brand {
    display: flex;
    align-items: center;
    gap: 12px;
    font-weight: 700;
    letter-spacing: 0.04em;
    text-transform: uppercase;
  }
  .brand__mark {
    width: 18px;
    height: 18px;
    background: currentColor;
  }
  .card--back .brand {
    color: #ffffff;
    font-size: 40px;
  }
  .card--front .brand {
    position: absolute;
    left: 36px;
    top: 48px;
    color: var(--dark-teal);
    font-size: 32px;
  }
  .contact {
    position: absolute;
    left: 190px;
    right: 28px;
    top: 168px;
    color: var(--ink);
  }
  .contact__heading {
    display: flex;
    align-items: baseline;
    gap: 8px;
    padding-bottom: 8px;
    border-bottom: 1px solid var(--rule);
    margin-bottom: 10px;
  }
  .contact__name {
    font-size: 22px;
    font-weight: 400;
    color: var(--teal-text);
    text-transform: uppercase;
    letter-spacing: 0.02em;
  }
  .contact__divider {
    font-size: 22px;
    color: var(--ink);
    font-weight: 500;
  }
  .contact__role {
    font-size: 14px;
    text-transform: uppercase;
    letter-spacing: 0.03em;
  }
  .contact__line {
    font-size: 13.5px;
    line-height: 1.35;
  }
  .contact__address {
    margin-top: 8px;
    font-size: 13.5px;
  }
  .contact__web {
    margin-top: 12px;
    font-size: 15px;
    color: var(--teal-text);
  }
</style>
</head>
<body>
  <section class="card card--back" aria-label="Business card back">
    <div class="brand"><span class="brand__mark"></span>CoreBit Systems</div>
  </section>

  <section class="card card--front" aria-label="Business card front">
    <div class="brand"><span class="brand__mark"></span>CoreBit Systems</div>
    <div class="contact">
      <div class="contact__heading">
        <span class="contact__name">Derek Fenwick</span>
        <span class="contact__divider">|</span>
        <span class="contact__role">Operations Manager</span>
      </div>
      <p class="contact__line">T: +44(0) 1632 xxx xxx | M: +44(0) 7700 xxx xxx</p>
      <p class="contact__line">E: derekf@corebitsys.example</p>
      <p class="contact__address">19 Tarlow Street, Aberdeen AB12 4QP</p>
      <p class="contact__web">www.corebitsys.example</p>
    </div>
  </section>
</body>
</html>
```